Wine and retail website for a high-end resort community

We are introducing a line of quality wines in the resort community of Martha's Vineyard, Massachusetts, USA. The site will detail information about the wine, and online store connected to and external government approved shipper for wine, and additional non-alcoholic retail merchandise sales.

We are planning the site to be driven off the Squarespace platform so I do not believe coding is necessary initially; however, the ability to do sop would be helpful if needed.

Attached are the images/files we have available so far. Please feel free to use stock images in your design.

Target Market(s)

Wine enthusiasts in the resort community of Martha’s Vineyard Massachusetts

Industry/Entity Type

Wine

Number of Pages Required

4 page

Font styles to use
Sans Serif

Requirements
Must have
• Home page, about page, wine page, e-commerce page, retail merchandise page. I recently came across brenthollwines.com and really like the look and layout of their pages if that helps
Nice to have
• A short wine/Martha’s Vineyard related video on the home page

```html
<!DOCTYPE html>
<html lang="en">
<head>
<meta charset="utf-8">
<title>Harrow Point Estates</title>
<link rel="stylesheet" href="https://fonts.googleapis.com/css2?family=Barlow:wght@400;500;600;700&family=Cormorant+Garamond:wght@500;600&family=Great+Vibes&display=swap">
<style>
:root{
  --maroon:#7b2335;
  --maroon-deep:#6b1f2f;
  --gold:#8d6b1f;
  --ink:#1d1a1a;
  --text:#3b3636;
  --muted:#777;
  --paper:#ffffff;
  --mist:#f1f1f1;
  --serif:"Cormorant Garamond", Georgia, serif;
  --script:"Great Vibes", cursive;
  --sans:"Barlow", Arial, sans-serif;
}
*{margin:0;padding:0;box-sizing:border-box}
html,body{width:1200px;height:4243px;overflow:hidden;background:var(--paper);font-family:var(--sans);color:var(--text)}
.page{position:relative;width:1200px;height:4243px;overflow:hidden}
.abs{position:absolute}
.script{font-family:var(--script);color:var(--maroon);font-size:46px;line-height:1;word-spacing:8px;white-space:nowrap}
.heading{font-family:var(--serif);font-weight:500;color:var(--ink);font-size:44px;letter-spacing:4px;line-height:1.05;text-transform:uppercase;white-space:nowrap}
.copy{font-size:16.5px;line-height:27px;color:var(--text)}
.copy p+p{margin-top:12px}
.btn{position:absolute;display:flex;align-items:center;justify-content:center;background:var(--maroon);color:#fff;font-weight:600;font-size:15px;letter-spacing:.5px;text-transform:uppercase;outline:2px solid var(--maroon);outline-offset:3px;border:1px solid #fff}
.btn.gold{background:var(--gold);outline-color:var(--gold)}
.photo{position:absolute}

.nav a{position:absolute;top:53px;font-size:14px;font-weight:500;color:var(--ink);text-decoration:none;letter-spacing:.3px}
.nav .active::after{content:"";position:absolute;left:0;right:0;top:24px;height:2px;background:var(--gold)}
.brand{position:absolute;left:470px;top:40px;width:260px;text-align:center;font-family:var(--serif);font-weight:600;color:var(--ink);font-size:28px;line-height:28px;letter-spacing:1px}
.brand small{display:block;font-size:11px;letter-spacing:6px;line-height:18px}

.hero-bg{left:0;top:0;width:1200px;height:720px;background:linear-gradient(180deg,#fff 0%,#e9e9e9 35%,#dcdcdc 55%,#f4f4f4 85%,#fff 100%)}
.welcome{left:130px;top:224px;width:528px;height:318px;border:1.5px solid #a86673;text-align:center}
.welcome .script{margin-top:30px;font-size:54px}
.welcome .title{font-family:var(--serif);font-weight:500;font-size:70px;line-height:64px;color:var(--ink);letter-spacing:5px;margin-top:10px}
.welcome .sub{font-family:var(--serif);font-size:24px;letter-spacing:11px;color:var(--ink);margin-top:12px}
.corner{position:absolute;background:var(--maroon)}

.feature{position:absolute;border:2px solid var(--maroon);background:#fff;text-align:center}
.feature h3{font-family:var(--serif);font-weight:500;font-size:26px;letter-spacing:1px;color:var(--ink);margin-top:66px}
.feature p{font-size:14px;line-height:20px;color:var(--muted);margin:8px 34px 0}
.feature.goldline{border-color:var(--gold)}
.feature.active{background:var(--maroon-deep);border:none;box-shadow:0 10px 20px rgba(0,0,0,.15)}
.feature.active h3,.feature.active p{color:#fff}
.icon-disc{position:absolute;width:82px;height:82px;border-radius:50%;display:flex;align-items:center;justify-content:center}

.product{position:absolute;width:308px;height:481px}
.product .top{position:absolute;left:0;top:0;width:308px;height:308px;background:var(--mist)}
.product .shot{position:absolute;left:104px;top:20px;width:100px;height:236px;background:linear-gradient(180deg,#6a2a34,#8c6a6e)}
.product .box{position:absolute;left:18px;top:258px;width:270px;height:223px;border:2px solid var(--maroon);background:#fff;text-align:center}
.product h4{font-size:17px;font-weight:700;color:var(--ink);margin-top:90px;letter-spacing:.3px}
.product p{font-size:15px;color:var(--text);margin-top:6px}

.footer{left:0;top:3794px;width:1200px;height:449px;background:linear-gradient(180deg,#1d1c1b,#141313)}
.fcol h5{font-family:var(--serif);font-weight:500;color:#fff;font-size:21px;letter-spacing:2.5px}
.fcol ul{list-style:none;margin-top:16px}
.fcol li{font-size:14px;color:#ddd;line-height:28px}
.contact-row{position:absolute;display:flex;align-items:center;gap:16px;color:#ddd;font-size:13.5px;line-height:20px}
.contact-row .dot{width:30px;height:30px;border-radius:50%;background:#fff;display:flex;align-items:center;justify-content:center;flex:none}
</style>
</head>
<body>
<div class="page">

  <div class="abs hero-bg" role="img" aria-label="Misty snow-capped mountain range in soft greys"></div>

  <nav class="nav">
    <a class="active" href="#" style="left:169px">HOME</a>
    <a href="#" style="left:250px">ABOUT US</a>
    <a href="#" style="left:361px">PRODUCTS</a>
    <a href="#" style="left:734px">SHOP NOW</a>
    <a href="#" style="left:848px">NEWS</a>
    <a href="#" style="left:932px">CONTACT</a>
    <a href="#" style="left:1030px;display:flex;align-items:center;gap:8px;top:50px">
      <svg width="28" height="24" viewBox="0 0 28 24" fill="none" stroke="#1d1a1a" stroke-width="2"><path d="M1 2h4l3 13h15l3-9H7"/><circle cx="10" cy="20" r="2"/><circle cx="21" cy="20" r="2"/></svg>
      <span style="font-size:13px">0 items</span>
    </a>
  </nav>
  <div class="brand">HARROW POINT<small>ESTATES</small></div>

  <div class="corner" style="left:120px;top:216px;width:95px;height:5px"></div>
  <div class="corner" style="left:120px;top:216px;width:5px;height:80px"></div>
  <div class="corner" style="left:658px;top:470px;width:5px;height:80px"></div>
  <div class="corner" style="left:568px;top:545px;width:95px;height:5px"></div>
  <div class="abs welcome">
    <div class="script">Welcome to</div>
    <div class="title">HARROW<br>POINT</div>
    <div class="sub">— ESTATES —</div>
  </div>
  <div class="btn" style="left:309px;top:521px;width:168px;height:44px">Learn More</div>

  <div class="photo" role="img" aria-label="Product photo: a bottle of red wine and a bottle of white wine" style="left:712px;top:96px;width:300px;height:540px;background:linear-gradient(90deg,#5a2430 0%,#8c6f73 45%,#9a9166 55%,#6b6230 100%);opacity:.9"></div>

  <div class="feature" style="left:124px;top:759px;width:310px;height:179px"><h3>OUR STORY</h3><p>Lorem ipsum dolor sit amet consecte tur adipiscing elit</p></div>
  <div class="feature active" style="left:453px;top:745px;width:311px;height:205px"><h3 style="margin-top:66px">PRODUCTS</h3><p>Lorem ipsum dolor sit amet consecte tur adipiscing elit</p>
    <svg width="18" height="12" viewBox="0 0 18 12" style="margin-top:12px" fill="none" stroke="#fff" stroke-width="2.5"><path d="M2 2l7 7 7-7"/></svg></div>
  <div class="feature goldline" style="left:781px;top:759px;width:310px;height:179px"><h3>WINE CLUB</h3><p>Lorem ipsum dolor sit amet consecte tur adipiscing elit</p></div>

  <div class="icon-disc" style="left:238px;top:725px;background:var(--maroon)"></div>
  <div class="icon-disc" style="left:567px;top:708px;background:#fff;border:2px solid var(--maroon)"></div>
  <div class="icon-disc" style="left:895px;top:725px;background:var(--gold)"></div>

  <div class="abs" style="left:0;top:1480px;width:1200px;height:230px;background:linear-gradient(180deg,#fff,#ececec 50%,#fff)" role="img" aria-label="Faint misty coastline in light grey"></div>
  <div class="abs" style="left:93px;top:1413px;width:129px;height:129px;border-radius:50%;background:var(--gold)"></div>
  <div class="photo" role="img" aria-label="Vineyard rows at golden sunset over rolling hills, with a video play button" style="left:129px;top:1025px;width:433px;height:483px;border-radius:216px 216px 0 0;background:linear-gradient(180deg,#f2d89a 0%,#c69a4e 30%,#7d6a2c 55%,#4b5220 80%,#3a3a1a 100%)"></div>
  <svg class="abs" style="left:307px;top:1240px" width="80" height="80" viewBox="0 0 80 80"><circle cx="40" cy="40" r="36" fill="none" stroke="#fff" stroke-width="5"/><path d="M31 25v30l24-15z" fill="#fff"/></svg>

  <div class="abs script" style="left:628px;top:1070px">Our Story</div>
  <h2 class="abs heading" style="left:626px;top:1120px">About Harrow<br>Point</h2>
  <svg class="abs" style="left:1028px;top:1190px" width="172" height="10"><rect x="0" y="1" width="8" height="8" fill="#7b2335"/><path d="M8 5h164" stroke="#7b2335" stroke-width="1.5"/></svg>
  <div class="abs copy" style="left:631px;top:1226px;width:470px">
    <p>Lorem ipsum dolor sit amet, consectetur adipiscing elit, sed do eiusmod tempor incididunt ut labore et dolore magna aliqua. Quis ipsum suspendisse ultrices gravida.</p>
    <p>Lorem ipsum dolor sit amet, consectetur adipiscing elit, sed do eiusmod tempor incididunt ut labore et dolore magna aliqua. Quis ipsum suspendisse ultrices gravida</p>
  </div>
  <div class="btn" style="left:633px;top:1427px;width:172px;height:44px">Learn More</div>

  <svg class="abs" style="left:598px;top:1572px" width="8" height="88"><path d="M4 0v78" stroke="#333" stroke-width="1.5"/><rect x="0" y="78" width="8" height="8" fill="#7b2335"/></svg>

  <div class="abs script" style="left:0;top:1688px;width:1200px;text-align:center">Our Wines</div>
  <h2 class="abs heading" style="left:0;top:1735px;width:1200px;text-align:center;font-size:42px;letter-spacing:5px">Our Products</h2>

  <div class="product" style="left:127px;top:1843px">
    <div class="top"></div>
    <div class="shot" role="img" aria-label="Product photo: red wine bottle"></div>
    <div class="box"><h4>WINE PRODUCT</h4><p>Lorem ipsum dolor sit amet con</p></div>
    <div class="btn gold" style="left:80px;top:407px;width:150px;height:36px;font-size:13px">Shop Now</div>
  </div>
  <div class="product" style="left:458px;top:1843px">
    <div class="top" role="img" aria-label="Deep red vineyard backdrop" style="background:linear-gradient(160deg,#8a2a33,#5e1a22)"></div>
    <div class="shot" role="img" aria-label="Product photo: white wine bottle" style="background:linear-gradient(180deg,#3b3a24,#a79c6a)"></div>
    <div class="box"><h4>WINE PRODUCT</h4><p>Lorem ipsum dolor sit amet con</p></div>
    <div class="btn gold" style="left:80px;top:407px;width:150px;height:36px;font-size:13px">Shop Now</div>
  </div>
  <div class="product" style="left:791px;top:1843px">
    <div class="top"></div>
    <div class="shot" role="img" aria-label="Product photo: red wine bottle"></div>
    <div class="box"><h4>WINE PRODUCT</h4><p>Lorem ipsum dolor sit amet con</p></div>
    <div class="btn gold" style="left:80px;top:407px;width:150px;height:36px;font-size:13px">Shop Now</div>
  </div>

  <div class="photo" role="img" aria-label="Two glasses of red wine beside grapes on an oak barrel, with a video play button" style="left:0;top:2393px;width:1200px;height:595px;background:linear-gradient(90deg,#000 0%,#000 27%,#3a2a10 42%,#7a6526 60%,#5a4a20 78%,#3b2a14 100%)"></div>
  <div class="abs" style="left:0;top:2975px;width:1200px;height:25px;background:#fff"></div>
  <svg class="abs" style="left:757px;top:2609px" width="112" height="112" viewBox="0 0 112 112"><circle cx="56" cy="56" r="54" fill="rgba(0,0,0,.55)"/><circle cx="56" cy="56" r="38" fill="none" stroke="#fff" stroke-width="6"/><path d="M47 38v36l28-18z" fill="#fff"/></svg>
  <svg class="abs" style="left:0;top:2605px" width="108" height="10"><path d="M0 5h100" stroke="#fff" stroke-width="1.5"/><rect x="100" y="1" width="8" height="8" fill="#fff"/></svg>
  <div class="abs script" style="left:135px;top:2538px;color:#fff">Why Our Wine</div>
  <h2 class="abs heading" style="left:137px;top:2588px;color:#fff">Inside Every Wine</h2>
  <div class="abs copy" style="left:140px;top:2652px;width:440px;color:#fff">
    <p>Lorem ipsum dolor sit amet, consectetur adipiscing elit, sed do eiusmod tempor incididunt ut labore et dolore magna aliqua. Quis ipsum suspendisse ultrices gravida.</p>
    <p>Lorem ipsum dolor sit amet, consectetur adipiscing elit, sed do eiusmod tempor incididunt ut labore et</p>
  </div>
  <div class="btn" style="left:147px;top:2827px;width:168px;height:44px">Learn More</div>

  <div class="abs" style="left:0;top:3300px;width:1200px;height:480px;background:linear-gradient(180deg,#fff,#f0f0f0 50%,#fff)" role="img" aria-label="Faint misty mountain texture"></div>
  <div class="photo" role="img" aria-label="Two hands raising glasses of red wine in a sunlit vineyard" style="left:104px;top:3095px;width:465px;height:275px;background:linear-gradient(135deg,#a8a24a,#6f7a2c 40%,#c9a650 75%,#8a6a2a)"></div>
  <div class="abs" style="left:82px;top:3370px;width:215px;height:185px;background:var(--gold)"></div>
  <div class="photo" role="img" aria-label="Group of friends toasting in a vineyard" style="left:302px;top:3370px;width:336px;height:239px;background:linear-gradient(180deg,#9ab06a,#5d7a38 55%,#7a8a4a)"></div>
  <div class="photo" role="img" aria-label="Product photo: red wine bottle" style="left:240px;top:3378px;width:76px;height:272px;background:linear-gradient(180deg,#6a2a34,#8c6a6e)"></div>
  <div class="abs script" style="left:679px;top:3144px">Our Story</div>
  <h2 class="abs heading" style="left:675px;top:3198px">Join the<br>Wine Society</h2>
  <div class="abs copy" style="left:681px;top:3300px;width:470px">
    <p>Lorem ipsum dolor sit amet, consectetur adipiscing elit, sed do eiusmod tempor incididunt ut labore et dolore magna aliqua. Quis ipsum suspendisse ultrices gravida.</p>
    <p>Lorem ipsum dolor sit amet, consectetur adipiscing elit, sed do eiusmod tempor incididunt ut labore et dolore magna aliqua. Quis ipsum suspendisse ultrices gravida</p>
  </div>
  <div class="btn" style="left:683px;top:3494px;width:167px;height:42px">Learn More</div>

  <footer class="abs footer">
    <div class="abs" style="left:358px;top:0;width:1px;height:340px;background:#3a3836"></div>
    <div class="abs" style="left:580px;top:0;width:1px;height:340px;background:#3a3836"></div>
    <div class="abs" style="left:811px;top:0;width:1px;height:340px;background:#3a3836"></div>

    <div class="abs" style="left:100px;top:110px;width:240px;text-align:center;font-family:var(--serif);font-weight:600;color:#fff;font-size:27px;line-height:27px;letter-spacing:1px">HARROW POINT<div style="font-size:11px;letter-spacing:6px;line-height:20px">ESTATES</div></div>
    <div class="abs" style="left:166px;top:200px;display:flex;gap:15px">
      <span style="width:34px;height:34px;border-radius:50%;background:#fff" aria-label="Social link"></span>
      <span style="width:34px;height:34px;border-radius:50%;background:var(--maroon)" aria-label="Social link"></span>
      <span style="width:34px;height:34px;border-radius:50%;background:#fff" aria-label="Social link"></span>
    </div>

    <div class="abs fcol" style="left:386px;top:76px"><h5>NAVIGATION</h5>
      <ul><li>About Us</li><li>Products</li><li>Shop Now</li><li>Why Our Wine</li><li>Blogs</li><li>Contact Us</li></ul></div>
    <div class="abs fcol" style="left:608px;top:76px"><h5>RESOURCES</h5>
      <ul><li>Cart</li><li>My Account</li><li>Wishlist</li><li>Support</li><li>Shipping &amp; Return</li><li>Help</li></ul></div>
    <div class="abs fcol" style="left:832px;top:76px"><h5>CONTACT US</h5></div>

    <div class="contact-row" style="left:834px;top:120px">
      <span class="dot"><svg width="14" height="18" viewBox="0 0 14 18"><path d="M7 0a7 7 0 0 0-7 7c0 5 7 11 7 11s7-6 7-11a7 7 0 0 0-7-7zm0 10a3 3 0 1 1 0-6 3 3 0 0 1 0 6z" fill="#1b1a19"/></svg></span>
      <span>214 Linden Hollow Lane,<br>Westbrook, MA 02575</span></div>
    <div class="contact-row" style="left:834px;top:176px">
      <span class="dot"><svg width="16" height="16" viewBox="0 0 16 16"><path d="M3 1l3 3-2 2c1 2 4 5 6 6l2-2 3 3-2 2C7 15 1 9 1 3z" fill="#1b1a19"/></svg></span>
      <span>(508) 555 0147</span></div>
    <div class="contact-row" style="left:834px;top:223px">
      <span class="dot"><svg width="16" height="12" viewBox="0 0 16 12" fill="none" stroke="#1b1a19" stroke-width="1.6"><rect x="1" y="1" width="14" height="10"/><path d="M1 1l7 6 7-6"/></svg></span>
      <span>hello@harrowpointestates.com</span></div>

    <div class="abs" style="left:0;top:342px;width:1200px;height:1px;background:#3a3836"></div>
    <div class="abs" style="left:125px;top:390px;font-size:12.5px;color:#ccc">© 2024 Harrow Point Estates. All Rights Reserved</div>
    <div class="abs" style="left:816px;top:390px;font-size:12.5px;color:#ccc;display:flex;gap:24px"><span>Terms of Use</span><span>Privacy Policy</span><span>FAQ</span></div>
  </footer>
</div>
</body>
</html>
```